Create Premium Wine Label Design

We are premium wine exporters from Australia. We are looking to introduce new brand " The Velloro" - in red wine, White wine and Sparkling wine to international market.

The sample label design for red wine ( Shiraz) is attached.

This is our luxury brand. We need a stunning wine label designs for (front, back and neck) that should be mostly in GOLD colour and design should be really eye catching.

We have provided sample design for front, back and neck labels. However, we are looking forward to see a completely new improvised design.

LOGO attached.

Front Label Design Specification:

* We would like to see designs that are in Gold colour.
* Wine Bottle size is standard: 750ml; we assume the same design can be resizable to different bottle sizes.
* Our design should suit both black, white and sparkling wine bottles(sample attached)
* Use our logo in the design (see attached - label sample)
* Content for front label (see attached).
* Design should include all information specified in the sample

Back Label Design
* All contents in the sample should be used ( sample attached)
* LOGO attached.

Neck Label Design
* Sample of Neck label attached, please provide similar or your own design.
* LOGO attached.

Image Samples:
* Samples of label designs we like (see attached)
* Sample for gold color (see attached)
* For bottle shapes (see attached)
* Front, Back and Neck Label Samples (see attached)

Target Market(s)

International Wine Market

Font styles to use
Decorative
Script

Requirements
Must have
• Must have golden color on front and back label

```html
<!DOCTYPE html>
<html lang="en">
<head>
<meta charset="utf-8">
<title>The Velloro Shiraz – Label Set</title>
<link rel="stylesheet" href="https://fonts.googleapis.com/css2?family=Cinzel:wght@600&family=Lobster&family=Berkshire+Swash&family=Open+Sans:wght@400;600&display=swap">
<style>
  :root {
    --bg: #e8e8e6;
    --label-dark: #1b1b1d;
    --band-slate: #2a323d;
    --gold: #d4a73c;
    --gold-light: #f3d27a;
    --gold-deep: #9a6d1c;
    --ink-light: #f2f2f2;
    --ink-soft: #c9c9c9;
  }
  * { margin: 0; padding: 0; box-sizing: border-box; }
  html, body { width: 1200px; height: 960px; overflow: hidden; background: var(--bg); }
  .canvas { position: relative; width: 1200px; height: 960px; }

  /* Neck label */
  .neck-label {
    position: absolute; left: 340px; top: 40px; width: 520px; height: 110px;
    background: var(--label-dark);
    border-top: 5px solid var(--gold);
    border-bottom: 5px solid var(--gold);
    box-shadow: inset 0 4px 0 var(--gold-deep), inset 0 -4px 0 var(--gold-deep);
    display: flex; flex-direction: column; align-items: center; justify-content: center; gap: 8px;
  }
  .neck-brand {
    font-family: "Cinzel", serif; font-weight: 600; font-size: 34px;
    letter-spacing: 3px; color: var(--gold);
  }
  .neck-rule { display: flex; align-items: center; gap: 8px; }
  .neck-rule span { display: block; width: 90px; height: 2px; background: var(--gold); }
  .neck-rule i { display: block; width: 9px; height: 9px; background: var(--gold); transform: rotate(45deg); }

  /* Front label */
  .front-label { position: absolute; left: 370px; top: 190px; width: 460px; height: 740px; }
  .label-frame { position: absolute; inset: 0; }
  .brand-seal {
    position: absolute; left: 168px; top: 33px; width: 124px; height: 124px;
    border-radius: 50%; border: 4px solid var(--gold);
    display: flex; align-items: center; justify-content: center; text-align: center;
    font-family: "Open Sans", sans-serif; font-weight: 600; font-size: 14px;
    letter-spacing: 1px; color: var(--gold); text-transform: uppercase; line-height: 1.3;
  }
  .varietal {
    position: absolute; left: 0; right: 0; top: 168px;
    display: flex; align-items: center; justify-content: center; gap: 14px;
  }
  .varietal .flourish { width: 50px; height: 2px; background: var(--gold); }
  .varietal h1 {
    font-family: "Lobster", cursive; font-weight: 400; font-size: 62px;
    color: var(--gold); line-height: 1;
  }
  .cuvee {
    position: absolute; left: 0; right: 0; top: 246px; text-align: center;
    font-family: "Berkshire Swash", cursive; font-size: 30px; color: var(--ink-light);
  }
  .gold-rule { position: absolute; left: 30px; right: 30px; height: 2px; background: var(--gold); }
  .tasting-note {
    position: absolute; left: 34px; right: 34px; top: 304px; text-align: center;
    font-family: "Open Sans", sans-serif; font-size: 12.5px; line-height: 1.75; color: var(--ink-light);
  }
  .product-facts {
    position: absolute; left: 36px; right: 36px; top: 442px;
    display: flex; justify-content: space-between; align-items: flex-end;
    font-family: "Open Sans", sans-serif; color: var(--ink-soft); font-size: 13px; line-height: 1.5;
  }
  .product-facts strong { color: var(--ink-light); font-weight: 600; font-size: 15px; }
  .volume { display: flex; align-items: center; gap: 6px; text-align: right; font-size: 12px; }
  .producer {
    position: absolute; left: 14px; right: 14px; top: 566px; height: 156px;
    background: var(--band-slate); border-top: 3px solid var(--gold);
    border-radius: 0 0 14px 14px;
    font-family: "Open Sans", sans-serif; text-align: center; color: var(--ink-light);
    padding-top: 26px;
  }
  .producer .company { font-weight: 600; font-size: 20px; }
  .producer .place { font-size: 15px; color: var(--ink-soft); margin-top: 6px; }
</style>
</head>
<body>
<main class="canvas">

  <section class="neck-label" aria-label="Neck label">
    <div class="neck-brand">KESTREL RIDGE</div>
    <div class="neck-rule"><span></span><i></i><span></span></div>
  </section>

  <section class="front-label" aria-label="Front label">
    <svg class="label-frame" width="460" height="740" viewBox="0 0 460 740" role="img" aria-label="Dark label ground with damask vine pattern and gold border">
      <defs>
        <linearGradient id="goldEdge" x1="0" y1="0" x2="1" y2="1">
          <stop offset="0" stop-color="#f3d27a"/>
          <stop offset="0.5" stop-color="#b8842a"/>
          <stop offset="1" stop-color="#f0c866"/>
        </linearGradient>
      </defs>
      <path d="M6,124 C24,124 34,104 34,84 C110,58 170,24 230,24 C290,24 350,58 426,84 C426,104 436,124 454,124 L454,714 Q454,734 434,734 L26,734 Q6,734 6,714 Z"
            fill="#1b1b1d" stroke="url(#goldEdge)" stroke-width="8"/>
      <path d="M16,132 C32,130 42,112 44,94 C116,70 172,38 230,38 C288,38 344,70 416,94 C418,112 428,130 444,132 L444,708 Q444,724 428,724 L32,724 Q16,724 16,708 Z"
            fill="none" stroke="#d4a73c" stroke-width="1.5"/>
    </svg>

    <div class="brand-seal">Kestrel<br>Ridge</div>

    <div class="varietal">
      <span class="flourish"></span>
      <h1>shiraz</h1>
      <span class="flourish"></span>
    </div>
    <div class="cuvee">The Velloro</div>

    <div class="gold-rule" style="top:294px"></div>
    <p class="tasting-note">Kestrel Ridge The Velloro is a Classic fruit driven wine bursting with aromas of dark fruits and spice with background notes of charred French oak. This is a full bodied wine showcasing rich and juicy dark fruits of plum and cherry balanced with soft tannins and oak, providing a long lasting finish. This wine matches perfectly with range of rich and hearty red meat or pasta dishes.</p>
    <div class="gold-rule" style="top:432px"></div>

    <div class="product-facts">
      <div>
        <strong>Product of Australia</strong><br>
        Preservative (220).<br>
        Antioxidant (300).<br>
        May Contain Traces of Milk.<br>
        Country of Origin : Australia
      </div>
      <div class="volume">
        <div>750 mL<br>12.5% Alc.</div>
        <svg width="16" height="30" viewBox="0 0 16 30" aria-hidden="true">
          <path d="M2,2 H14 Q14,14 8,15 Q2,14 2,2 Z M8,15 V27 M3,28 H13" fill="none" stroke="#f2f2f2" stroke-width="1.6"/>
        </svg>
      </div>
    </div>

    <div class="producer">
      <div class="company">Kestrel Ridge Wines Pty. Ltd.,</div>
      <div class="place">Wattle Creek, Victoria, Australia</div>
    </div>
  </section>

</main>
</body>
</html>
```